Create a website for a car broker/car buyers advocate

build a website to suit a car brokering/car buying service. The design should communicate saving people time, money and stress by outsourcing the purchasing process for thier new car. I woudl like a modern site which is scroll able all on one page and wouldnt mind a dark or minimalistic theme. i have uploaded the logo which has also been designed by pixel harbor

Target Market(s)

general consumers, new car buyers, car collectors

Industry/Entity Type

Car Dealer

Font styles to use
Sans Serif

Colors

Designer to choose colors to be used in the design.

Requirements
Must have
• single page scrollable site
• modern design
• professional but fun
Nice to have
• some websites i like of similar businesses are :
• http://www.motorvane.com.au/
• https://drivelynx.com.au/

```html
<!DOCTYPE html>
<html lang="en">
<head>
<meta charset="utf-8">
<title>Torva Brokers — Car Brokering &amp; Car Buying Service</title>
<link rel="stylesheet" href="https://fonts.googleapis.com/css2?family=Poppins:wght@300;400;500;600&family=Roboto:wght@400;500;700;900&display=swap">
<style>
:root{
  --accent:#7d93c6;
  --accent-dark:#4e5b86;
  --navy:#46506e;
  --ink:#1f2126;
  --text:#555a63;
  --muted:#8a8f98;
  --white:#ffffff;
  --footer:#1d1e22;
  --star:#e5532b;
  --line:#d9dce3;
}
*{box-sizing:border-box;margin:0;padding:0}
html,body{width:1200px;height:4402px;overflow:hidden;background:var(--white)}
body{position:relative;font-family:"Poppins",sans-serif;color:var(--text)}
.abs{position:absolute}
a{color:inherit;text-decoration:none}

/* Hero */
.hero{position:absolute;left:0;top:0;width:1200px;height:670px;
  clip-path:polygon(0 0,100% 0,100% 607px,1128px 670px,72px 670px,0 607px);
  background:linear-gradient(100deg,#3a4348 0%,#5b5d5c 35%,#4a4f55 60%,#2c3238 100%)}
.hero-photo{position:absolute;inset:0;background:radial-gradient(ellipse at 38% 30%,rgba(190,150,125,.45),transparent 45%),radial-gradient(ellipse at 70% 25%,rgba(170,135,110,.4),transparent 40%),linear-gradient(180deg,rgba(20,24,30,.25),rgba(20,24,30,.55))}
.brand{position:absolute;display:flex;align-items:center;gap:12px;color:var(--white);font-family:"Poppins",sans-serif;font-weight:500;letter-spacing:6px;font-size:18px}
.brand .mark{width:22px;height:22px;background:var(--white)}
.call{left:604px;top:40px;display:flex;align-items:center;gap:10px;color:var(--white)}
.call .ring{width:40px;height:40px;border:2px solid var(--white);border-radius:50%;display:flex;align-items:center;justify-content:center}
.call small{display:block;font-size:16px;line-height:18px}
.call strong{display:block;font-family:"Roboto",sans-serif;font-size:20px;font-weight:700;line-height:24px}
.btn-estimate{left:824px;top:38px;width:230px;height:39px;background:var(--accent);color:var(--white);font-family:"Roboto",sans-serif;font-weight:500;font-size:15px;display:flex;align-items:center;justify-content:center;border-radius:2px}
.nav{left:470px;top:112px;display:flex;gap:30px;color:var(--white);font-family:"Roboto",sans-serif;font-weight:500;font-size:15px;letter-spacing:.3px}
.hero-title{left:0;top:270px;width:1200px;text-align:center;color:var(--white);font-family:"Roboto",sans-serif;font-weight:700;font-size:60px;letter-spacing:-.5px}
.hero-sub{left:0;top:352px;width:1200px;text-align:center;color:var(--white);font-size:19px;line-height:36px}
.hero-down{left:580px;top:446px;width:40px;height:40px;border:2px solid var(--white);border-radius:50%;display:flex;align-items:center;justify-content:center}
.select{top:578px;height:42px;border:2px solid rgba(255,255,255,.85);border-radius:22px;color:var(--white);font-size:12px;display:flex;align-items:center;justify-content:space-between;padding:0 18px}
.btn-start{left:863px;top:578px;width:191px;height:42px;border-radius:22px;background:var(--accent);color:var(--white);font-family:"Roboto",sans-serif;font-weight:500;font-size:17px;display:flex;align-items:center;justify-content:center}

/* Welcome */
.welcome-frame{left:145px;top:762px;width:376px;height:328px;border:2px solid var(--accent-dark)}
.welcome-photo{left:162px;top:779px;width:392px;height:349px;background:linear-gradient(135deg,#8fa08a 0%,#b6b7b2 40%,#6f88a8 60%,#3b4150 100%)}
.welcome-title{left:608px;top:776px;font-family:"Roboto",sans-serif;font-weight:700;font-size:38px;color:var(--ink)}
.welcome-title span{color:var(--accent);font-weight:500}
.welcome-text{left:608px;top:838px;width:450px;font-size:14px;line-height:30.4px;color:var(--text)}
.btn-outline{left:608px;top:1075px;width:130px;height:38px;border:2px solid var(--navy);color:var(--navy);font-family:"Roboto",sans-serif;font-weight:500;font-size:15px;display:flex;align-items:center;justify-content:center;border-radius:2px}

/* Banded sections */
.band{position:absolute;left:0;width:1200px;
  clip-path:polygon(0 63px,131px 0,1069px 0,1200px 63px,1200px calc(100% - 63px),1069px 100%,131px 100%,0 calc(100% - 63px))}
.services{top:1227px;height:636px;background:linear-gradient(90deg,#4a5472 0%,#4d5775 60%,#5d6783 80%,#4a5472 100%)}
.section-title{position:absolute;left:0;width:1200px;text-align:center;font-family:"Roboto",sans-serif;font-size:38px;color:var(--ink)}
.section-title b{font-weight:900}
.section-title span{font-weight:400}
.section-title.light{color:var(--white)}
.section-title .blue{color:var(--accent);font-weight:700}
.services .lead{left:0;top:133px;width:1200px;text-align:center;color:var(--white);font-size:16px}
.svc{top:250px;width:285px;height:273px;border:2px solid rgba(255,255,255,.85);color:var(--white);text-align:center}
.svc .icon{position:absolute;left:94px;top:-45px;width:96px;height:96px;border-radius:50%;background:var(--accent);border:3px solid var(--white);display:flex;align-items:center;justify-content:center}
.svc h3{margin-top:78px;font-family:"Roboto",sans-serif;font-weight:700;font-size:18px}
.svc p{margin:14px auto 0;width:256px;font-size:13px;line-height:25.5px;color:#e4e7ef}
.svc a{display:inline-block;margin-top:8px;font-size:13px;text-decoration:underline}

/* Best cars */
.title-rule{left:553px;width:94px;height:3px;background:var(--navy)}
.car-photo{width:285px;height:219px;box-shadow:0 8px 14px rgba(0,0,0,.2)}
.car-caption{width:285px;text-align:center;font-size:13.5px;line-height:24px;color:#333}

/* Insurance */
.insurance{top:2805px;height:416px;background:linear-gradient(90deg,#2a2d33 0%,#3a3d43 40%,#2d3036 100%)}
.insurance .sub{left:0;top:198px;width:1200px;text-align:center;color:var(--white);font-size:16px}
.email{left:318px;top:247px;width:412px;height:40px;border-radius:20px;background:var(--white);font-size:11px;color:#777;display:flex;align-items:center;padding-left:18px}
.btn-sub{left:752px;top:247px;width:130px;height:40px;border-radius:20px;background:var(--accent);color:var(--white);font-family:"Roboto",sans-serif;font-weight:700;font-size:14px;display:flex;align-items:center;justify-content:center}

/* Testimonials */
.quote{width:268px;font-size:12.5px;line-height:23.5px;color:#444}
.quote svg{vertical-align:-2px;margin-right:8px}
.avatar{width:72px;height:72px;border-radius:50%;background:linear-gradient(160deg,#c9ccd2,#59616e)}
.who{font-size:14px;line-height:26px;color:#555}
.who .name{color:var(--navy)}
.stars{color:var(--star);font-size:13px;letter-spacing:5px}
.arrow-round{width:26px;height:26px;border-radius:50%;background:#8e939b;display:flex;align-items:center;justify-content:center}

/* Footer */
.footer{position:absolute;left:0;top:3746px;width:1200px;height:656px;background:var(--footer);
  clip-path:polygon(0 62px,131px 0,1069px 0,1200px 62px,100% 100%,0 100%)}
.partner{top:82px;width:175px;height:77px;background:var(--white);display:flex;align-items:center;justify-content:center;font-family:"Poppins",sans-serif;font-weight:600;font-size:17px;color:#333}
.foot-brand{left:142px;top:240px;color:#4d5775;font-size:17px;letter-spacing:6px}
.foot-brand .mark{background:#4d5775}
.foot-about{left:142px;top:338px;width:380px;font-size:12px;line-height:21px;color:var(--white)}
.foot-head{font-family:"Roboto",sans-serif;font-weight:700;font-size:20px;color:var(--white)}
.foot-list{list-style:none;font-size:13.5px;color:var(--white)}
.contact li{display:flex;gap:14px;line-height:17px;margin-bottom:15px}
.contact svg{flex:none;margin-top:1px}
.links li{line-height:29px}
.socials{left:515px;top:528px;display:flex;gap:8px}
.socials span{width:28px;height:28px;border:1.5px solid var(--white);border-radius:50%;display:flex;align-items:center;justify-content:center}
.socials span i{width:8px;height:8px;border-radius:50%;background:var(--white)}
.copyright{left:0;top:578px;width:1200px;text-align:center;color:var(--white);font-size:13.5px}
</style>
</head>
<body>

<!-- Hero -->
<header class="hero">
  <div class="hero-photo" role="img" aria-label="Smiling couple at a car dealership being helped by a broker"></div>
  <div class="brand" style="left:142px;top:66px"><span class="mark"></span>TORVA BROKERS</div>
  <div class="abs call">
    <span class="ring"><svg width="20" height="20" viewBox="0 0 24 24" fill="none" stroke="#fff" stroke-width="2"><path d="M5 3h4l2 5-3 2a11 11 0 0 0 6 6l2-3 5 2v4a2 2 0 0 1-2 2A17 17 0 0 1 3 5a2 2 0 0 1 2-2z"/></svg></span>
    <div><small>Call Us</small><strong>(808) 555-0172</strong></div>
  </div>
  <a class="abs btn-estimate" href="#">REQUEST A FREE ESTIMATE</a>
  <nav class="abs nav"><a href="#">HOME</a><a href="#">ABOUT TORVA BROKERS</a><a href="#">BEST CARS</a><a href="#">FINANCE</a><a href="#">CONTACT US</a></nav>
  <h1 class="abs hero-title">TORVA BROKERS</h1>
  <p class="abs hero-sub">We are a car brokering/car buying service<br>voluptatem quia voluptas sit aspernatur&nbsp; consequuntur</p>
  <div class="abs hero-down"><svg width="16" height="10" viewBox="0 0 16 10" fill="none" stroke="#fff" stroke-width="2"><path d="M1 1l7 7 7-7"/></svg></div>
  <div class="abs select" style="left:143px;width:224px">New/Used<svg width="10" height="6" viewBox="0 0 10 6" fill="none" stroke="#fff" stroke-width="1.6"><path d="M1 1l4 4 4-4"/></svg></div>
  <div class="abs select" style="left:384px;width:223px">Select the Make<svg width="10" height="6" viewBox="0 0 10 6" fill="none" stroke="#fff" stroke-width="1.6"><path d="M1 1l4 4 4-4"/></svg></div>
  <div class="abs select" style="left:624px;width:223px">Select the Model<svg width="10" height="6" viewBox="0 0 10 6" fill="none" stroke="#fff" stroke-width="1.6"><path d="M1 1l4 4 4-4"/></svg></div>
  <a class="abs btn-start" href="#">Click Here To Start</a>
</header>

<!-- Welcome -->
<section>
  <div class="abs welcome-frame"></div>
  <div class="abs welcome-photo" role="img" aria-label="Happy couple holding up new car keys beside their car"></div>
  <h2 class="abs welcome-title">Welcome to <span>Torva Brokers</span></h2>
  <p class="abs welcome-text">Sed ut perspiciatis unde omnis iste natus error sit voluptatem accusantium doloremque laudantium, totam rem aperiam, eaque ipsa quae ab illo inventore veritatis et quasi architecto beatae vitae dicta sunt explicabo. Nemo enim ipsam voluptatem quia voluptas sit aspernatur aut odit aut fugit, sed quia consequuntur magni dolores eos qui ratione voluptatem sequi nesciunt. Neque porro quisquam est, qui dolorem ipsum quia dolor</p>
  <a class="abs btn-outline" href="#">READ MORE</a>
</section>

<!-- Services -->
<section class="band services" role="img" aria-label="Dark blue band over a faded photo of a car">
  <h2 class="section-title light" style="top:73px"><b>OUR</b> <span>SERVICES</span></h2>
  <p class="abs lead">Nemo enim ipsam voluptatem quia voluptas sit</p>
  <div class="abs svc" style="left:143px">
    <div class="icon"><svg width="44" height="44" viewBox="0 0 44 44" fill="none" stroke="#fff" stroke-width="2"><path d="M22 26V12"/><circle cx="22" cy="10" r="5"/><path d="M6 30h10l6 4h14M6 36h30"/></svg></div>
    <h3>IS THIS YOU?</h3>
    <p>Sed ut perspiciatis unde omnis iste natus error sit voluptatem accusantium doloremque laudantium, totam rem aperiam, eaque ipsa quae ab</p>
    <a href="#">Read More</a>
  </div>
  <div class="abs svc" style="left:455px">
    <div class="icon"><svg width="44" height="44" viewBox="0 0 44 44" fill="none" stroke="#fff" stroke-width="2"><rect x="20" y="6" width="18" height="12" rx="2"/><path d="M24 18l-2 4 5-4"/><circle cx="15" cy="20" r="6"/><path d="M5 38c0-7 4-11 10-11s10 4 10 11"/></svg></div>
    <h3>WE CAN HELP YOU!</h3>
    <p>Sed ut perspiciatis unde omnis iste natus error sit voluptatem accusantium doloremque laudantium, totam rem aperiam, eaque ipsa quae ab</p>
    <a href="#">Read More</a>
  </div>
  <div class="abs svc" style="left:769px">
    <div class="icon"><svg width="44" height="44" viewBox="0 0 44 44" fill="none" stroke="#fff" stroke-width="2"><path d="M6 30l4-9h24l4 9v6H6z"/><circle cx="13" cy="32" r="2"/><circle cx="31" cy="32" r="2"/><path d="M26 6l8 3v6c0 4-4 6-8 7-4-1-8-3-8-7V9z"/><path d="M23 14l2 2 4-4"/></svg></div>
    <h3>NEW WAY OF BUYING A CAR</h3>
    <p>Sed ut perspiciatis unde omnis iste natus error sit voluptatem accusantium doloremque laudantium, totam rem aperiam, eaque ipsa quae ab</p>
    <a href="#">Read More</a>
  </div>
</section>

<!-- Best cars -->
<section>
  <h2 class="section-title" style="top:1953px"><b>BEST</b> <span class="blue">CARS</span></h2>
  <div class="abs title-rule" style="top:2026px"></div>

  <div class="abs car-photo" style="left:143px;top:2071px;background:linear-gradient(180deg,#5f8fc9 0%,#cfd7dc 50%,#e0a34e 70%,#6b6b5d 100%)" role="img" aria-label="Silver hatchback on a road at sunset"></div>
  <div class="abs car-photo" style="left:457px;top:2071px;background:linear-gradient(180deg,#c7d3d6 0%,#7f9465 45%,#3d4b32 70%,#4f5455 100%)" role="img" aria-label="White SUV driving through green hills"></div>
  <div class="abs car-photo" style="left:771px;top:2071px;background:linear-gradient(180deg,#8e9294 0%,#5d6164 45%,#1d1f22 70%,#6b6d6e 100%)" role="img" aria-label="Black luxury coupe on a blurred road"></div>
  <p class="abs car-caption" style="left:143px;top:2316px">Sed ut perspiciatis unde omnis iste natus error sit voluptatem accusantium</p>
  <p class="abs car-caption" style="left:457px;top:2316px">Sed ut perspiciatis unde omnis iste natus error sit voluptatem accusantium</p>
  <p class="abs car-caption" style="left:771px;top:2316px">Sed ut perspiciatis unde omnis iste natus error sit voluptatem accusantium</p>

  <div class="abs car-photo" style="left:143px;top:2393px;background:linear-gradient(180deg,#2c2e30 0%,#d9b41c 45%,#2a2b2c 75%,#4a4b4c 100%)" role="img" aria-label="Yellow sports car with black stripes"></div>
  <div class="abs car-photo" style="left:457px;top:2393px;background:linear-gradient(135deg,#55627a 0%,#9a8a5a 35%,#d9dde0 55%,#4b5158 100%)" role="img" aria-label="White sedan cornering on a mountain road"></div>
  <div class="abs car-photo" style="left:771px;top:2393px;background:linear-gradient(180deg,#c8d0d6 0%,#8c9aa4 40%,#a01f24 60%,#5a5d60 100%)" role="img" aria-label="Red coupe driving along a coastal highway"></div>
  <p class="abs car-caption" style="left:143px;top:2644px">Sed ut perspiciatis unde omnis iste natus error sit voluptatem accusantium</p>
  <p class="abs car-caption" style="left:457px;top:2644px">Sed ut perspiciatis unde omnis iste natus error sit voluptatem accusantium</p>
  <p class="abs car-caption" style="left:771px;top:2644px">Sed ut perspiciatis unde omnis iste natus error sit voluptatem accusantium</p>
</section>

<!-- Insurance -->
<section class="band insurance" role="img" aria-label="Dark band over a faded photo of a couple with car keys">
  <h2 class="section-title light" style="top:130px;font-weight:700;font-size:40px;letter-spacing:.5px">DISCOUNT CAR INSURANCE</h2>
  <p class="abs sub">Stay up to date with the latest news.</p>
  <div class="abs email">Enter Your Email</div>
  <a class="abs btn-sub" href="#">SUBSCRIBE</a>
</section>

<!-- Testimonials -->
<section>
  <h2 class="section-title" style="top:3297px;letter-spacing:1.5px"><b>OUR CLIENTS</b> <span>SAYS</span></h2>
  <div class="abs title-rule" style="left:573px;width:78px;top:3375px;background:var(--accent)"></div>
  <div class="abs arrow-round" style="left:76px;top:3507px"><svg width="8" height="12" viewBox="0 0 8 12" fill="none" stroke="#fff" stroke-width="2"><path d="M6 1L1 6l5 5"/></svg></div>
  <div class="abs arrow-round" style="left:1094px;top:3507px"><svg width="8" height="12" viewBox="0 0 8 12" fill="none" stroke="#fff" stroke-width="2"><path d="M2 1l5 5-5 5"/></svg></div>

  <p class="abs quote" style="left:140px;top:3443px"><svg width="22" height="16" viewBox="0 0 22 16" fill="#c9ccd2"><rect x="0" y="0" width="9" height="9"/><rect x="12" y="0" width="9" height="9"/><path d="M9 7l-4 9H2l3-9zM21 7l-4 9h-3l3-9z"/></svg>Sed ut perspiciatis unde omnis iste natus error sit voluptatem accusantium dolemque laudantium, totam rem aperiam, eaque ipsa quae ab illo inventore</p>
  <p class="abs quote" style="left:475px;top:3443px"><svg width="22" height="16" viewBox="0 0 22 16" fill="#c9ccd2"><rect x="0" y="0" width="9" height="9"/><rect x="12" y="0" width="9" height="9"/><path d="M9 7l-4 9H2l3-9zM21 7l-4 9h-3l3-9z"/></svg>Sed ut perspiciatis unde omnis iste natus error sit voluptatem accusantium dolemque laudantium, totam rem aperiam, eaque ipsa quae ab illo inventore</p>
  <p class="abs quote" style="left:810px;top:3443px"><svg width="22" height="16" viewBox="0 0 22 16" fill="#c9ccd2"><rect x="0" y="0" width="9" height="9"/><rect x="12" y="0" width="9" height="9"/><path d="M9 7l-4 9H2l3-9zM21 7l-4 9h-3l3-9z"/></svg>Sed ut perspiciatis unde omnis iste natus error sit voluptatem accusantium dolemque laudantium, totam rem aperiam, eaque ipsa quae ab illo inventore</p>

  <div class="abs avatar" style="left:140px;top:3562px" role="img" aria-label="Client portrait"></div>
  <div class="abs who" style="left:233px;top:3557px"><div class="name">Nora P</div><div>Torva Brokers</div><div class="stars">★★★★★</div></div>
  <div class="abs avatar" style="left:475px;top:3562px" role="img" aria-label="Client portrait"></div>
  <div class="abs who" style="left:568px;top:3557px"><div class="name">Nora P</div><div>Torva Brokers</div><div class="stars">★★★★★</div></div>
  <div class="abs avatar" style="left:810px;top:3562px" role="img" aria-label="Client portrait"></div>
  <div class="abs who" style="left:903px;top:3557px"><div class="name">Nora P</div><div>Torva Brokers</div><div class="stars">★★★★★</div></div>
</section>

<!-- Footer -->
<footer class="footer">
  <svg class="abs" style="left:86px;top:106px" width="16" height="30" viewBox="0 0 16 30" fill="none" stroke="#9a9ea6" stroke-width="2"><path d="M14 1L2 15l12 14"/></svg>
  <svg class="abs" style="left:1088px;top:106px" width="16" height="30" viewBox="0 0 16 30" fill="none" stroke="#9a9ea6" stroke-width="2"><path d="M2 1l12 14L2 29"/></svg>
  <div class="abs partner" style="left:130px">Norvale</div>
  <div class="abs partner" style="left:321px">Cloudwick</div>
  <div class="abs partner" style="left:511px">Yondo</div>
  <div class="abs partner" style="left:701px">Beacon News</div>
  <div class="abs partner" style="left:890px">Techloom</div>

  <div class="brand foot-brand"><span class="mark"></span>TORVA BROKERS</div>
  <p class="abs foot-about">Sed ut perspiciatis unde omnis iste natus error sit voluptatem accusantium doloremque laudantium, totam rem aperiam, eaque ipsa quae ab illo inventore veritatis et quasi architecto beatae vitae dicta sunt explicabo.</p>

  <h3 class="abs foot-head" style="left:603px;top:225px">CONTACT US</h3>
  <ul class="abs foot-list contact" style="left:603px;top:280px;width:270px">
    <li><svg width="14" height="16" viewBox="0 0 14 16" fill="none" stroke="#fff" stroke-width="1.4"><path d="M7 15s5-5 5-9A5 5 0 0 0 2 6c0 4 5 9 5 9z"/><circle cx="7" cy="6" r="2"/></svg><span>Torva Brokers<br>14 Harbour Lane Unit #2<br>Location.</span></li>
    <li><svg width="14" height="14" viewBox="0 0 24 24" fill="none" stroke="#fff" stroke-width="2"><path d="M5 3h4l2 5-3 2a11 11 0 0 0 6 6l2-3 5 2v4a2 2 0 0 1-2 2A17 17 0 0 1 3 5a2 2 0 0 1 2-2z"/></svg><span>Phone :&nbsp; +999 6544 0190</span></li>
    <li><svg width="15" height="12" viewBox="0 0 15 12" fill="none" stroke="#fff" stroke-width="1.4"><rect x="1" y="1" width="13" height="10"/><path d="M1 1l6.5 5L14 1"/></svg><span>Email : info@torvabrokers.com</span></li>
  </ul>

  <h3 class="abs foot-head" style="left:928px;top:225px">QUICK LINKS</h3>
  <ul class="abs foot-list links" style="left:928px;top:270px">
    <li>Home</li><li>About Torva Brokers</li><li>Best Cars</li><li>Finance</li><li>Contact Us</li>
  </ul>

  <div class="abs socials"><span><i></i></span><span><i></i></span><span><i></i></span><span><i></i></span></div>
  <p class="abs copyright">Copyright © Torva Brokers. 2019. All rights reserved.</p>
</footer>

</body>
</html>
```